New name flyer

We have just changed our business name from kL Property group to Harbour Lane. We want to distribute a flyer to the local community to inform them of the change. We are a realestate agency which focuses mainly on property management but also sales. We service from Brisbane to the Sunshine coast.

Target Market(s)

Local community

Industry/Entity Type

realestate

Requirements
Must have
• Details of name change
Nice to have
• Servicing area Brisbane and Sunshine Coast, no change in management or services we offer, and will continue pride ourselves on offering a high level of service, with the same team from the Gold to Sunshine Coast.
Should not have
• too much wording.

```html
<!DOCTYPE html>
<html lang="en">
<head>
<meta charset="utf-8">
<title>Harbour Lane – New Name Flyer</title>
<link rel="stylesheet" href="https://fonts.googleapis.com/css2?family=Montserrat:ital,wght@0,400;0,600;0,700;0,800;1,400&display=swap">
<style>
  :root {
    --navy: #0a1b7a;
    --gold: #c9971c;
    --paper: #e7e7e7;
    --paper-light: #f2f2f2;
    --white: #ffffff;
  }
  html, body { margin: 0; padding: 0; overflow: hidden; }
  body { width: 845px; height: 1200px; background: var(--paper); }
  .flyer {
    position: relative;
    width: 845px;
    height: 1200px;
    overflow: hidden;
    background: var(--paper);
    font-family: "Montserrat", sans-serif;
  }
  .flyer__art { position: absolute; inset: 0; }
  .brand {
    position: absolute;
    left: 520px;
    top: 148px;
    width: 300px;
    text-align: center;
    margin: 0;
    font-family: "Montserrat", sans-serif;
    font-weight: 600;
    font-size: 28px;
    letter-spacing: 1px;
    color: var(--navy);
  }
  .intro {
    position: absolute;
    left: 60px;
    top: 602px;
    margin: 0;
    font-style: italic;
    font-weight: 400;
    font-size: 33px;
    line-height: 40px;
    color: var(--gold);
  }
  .headline {
    position: absolute;
    left: 58px;
    top: 692px;
    margin: 0;
    font-weight: 800;
    font-size: 58px;
    line-height: 66px;
    color: var(--navy);
  }
  .message {
    position: absolute;
    left: 0;
    width: 845px;
    text-align: center;
    margin: 0;
  }
  .message--body {
    top: 890px;
    font-weight: 400;
    font-size: 24px;
    line-height: 29px;
    color: var(--white);
  }
  .message--promise {
    top: 1022px;
    font-weight: 700;
    font-size: 25px;
    line-height: 31px;
    color: var(--gold);
  }
</style>
</head>
<body>
<main class="flyer">
  <svg class="flyer__art" width="845" height="1200" viewBox="0 0 845 1200" xmlns="http://www.w3.org/2000/svg">
    <defs>
      <linearGradient id="cityscape" x1="0" y1="0" x2="0" y2="1">
        <stop offset="0" stop-color="#7f9be8"/>
        <stop offset="0.3" stop-color="#d7b9d6"/>
        <stop offset="0.48" stop-color="#f2c79a"/>
        <stop offset="0.62" stop-color="#8b8a86"/>
        <stop offset="0.8" stop-color="#b9b3a4"/>
        <stop offset="1" stop-color="#6f7072"/>
      </linearGradient>
    </defs>

    <path role="img" aria-label="Photo of a city skyline and rooftops at sunset"
          d="M0 0 H620 V380 C520 520 390 590 235 590 C140 590 60 565 0 528 Z"
          fill="url(#cityscape)"/>
    <path class="photo-edge" d="M0 528 C60 565 140 590 235 590 C390 590 520 520 620 380"
          fill="none" stroke="var(--navy)" stroke-width="9"/>

    <circle cx="672" cy="180" r="232" fill="var(--navy)"/>
    <circle cx="672" cy="180" r="222" fill="var(--gold)"/>
    <circle cx="672" cy="180" r="216" fill="var(--paper-light)"/>

    <path class="wave" d="M0 808 C190 770 390 822 560 852 C700 876 800 830 845 742 V1200 H0 Z"
          fill="var(--navy)"/>

    <rect x="0" y="1126" width="845" height="2" fill="var(--gold)"/>
    <rect x="0" y="1132" width="845" height="2" fill="var(--gold)"/>
    <rect x="0" y="1139" width="845" height="5" fill="var(--gold)"/>
  </svg>

  <p class="brand">HARBOUR LANE</p>

  <p class="intro">We are excited<br>to let you know that kL Property,</p>
  <h1 class="headline">Is Now Harbour Lane</h1>

  <p class="message message--body">YES!!! We have just changed the name, Your favourite<br>management team and nature of our business and<br>services remains the same.</p>
  <p class="message message--promise">We will continue to serve you the same great service<br>from Brisbane to the Sunshine Coast</p>
</main>
</body>
</html>
```